Empresa de Asesoramiento en inversiones necesita un nuevo diseño de web

Necesitamos un nuevo diseño de pagina web que nos permita impulsar el posicionamiento de marca en los clientes.
Somos una empresa Española que busca, coordina y gestiona las alternativas de inversión que mejor se ajustan a las necesidades de los Clientes extranjeros, no residentes, para que puedan compra viviendas, locales comerciales o realizar inversiones en sociedades y startup en España.
En la actualidad tenemos esta web que puede servir de referencia; www.ferolanvexa,com
El diseño final debe comunicar seguridad y responsabilidad en los procesos de inversión.
Necesitamos que la Pagina web sea bilingüe ( Español-Ingles)

```html
<!DOCTYPE html>
<html lang="en">
<head>
<meta charset="utf-8">
<title>FerolanVexa – Investment in Spain</title>
<link rel="stylesheet" href="https://fonts.googleapis.com/css2?family=Libre+Caslon+Text:wght@400;700&family=Lato:wght@400;700&family=Poppins:wght@400;500;600&display=swap">
<style>
:root{
  --navy:#0b0d57;
  --navy-deep:#0f113a;
  --red:#b3313d;
  --grey:#6c6c6c;
  --ink:#1d1d1d;
  --line:#b9b9c4;
  --white:#ffffff;
}
*{box-sizing:border-box;margin:0;padding:0}
html,body{width:1200px;height:3972px;overflow:hidden}
body{position:relative;background:var(--white);font-family:"Poppins",sans-serif;color:var(--ink)}
.abs{position:absolute}
.serif{font-family:"Libre Caslon Text",serif}

/* header */
.brand-box{position:absolute;border:2px solid #333;display:flex;align-items:center;justify-content:center;font-family:"Lato",sans-serif;font-size:32px;letter-spacing:1.5px;color:#333;background:#fff}
.lang{position:absolute;left:1052px;top:32px;display:flex;align-items:center;gap:6px;padding:3px 6px;border:1px solid #ddd;font-family:"Lato",sans-serif;font-weight:700;font-size:20px}
.lang i{display:block;width:24px;height:20px;background:var(--navy)}
.nav{position:absolute;left:0;width:1200px;display:flex;justify-content:center;align-items:center;font-family:"Lato",sans-serif;font-size:20px;color:#fff}
.nav span{padding:0 36px}
.nav b{font-weight:400;opacity:.85}

/* hero */
.hero{left:0;top:170px;width:1200px;height:683px;background:linear-gradient(180deg,#3c4a86 0%,#5a5a8c 45%,#6e5c6e 75%,#2b2f55 100%)}
.hero h1{position:absolute;top:390px;width:1200px;text-align:center;font-family:"Libre Caslon Text",serif;font-weight:400;font-size:92px;color:#fff}
.hero-sub{position:absolute;top:505px;width:1200px;text-align:center;font-size:30px;color:#fff;font-family:"Lato",sans-serif}
.hero-btn{position:absolute;left:540px;top:574px;width:136px;height:43px;border:2px solid #fff;border-radius:6px;color:#fff;font-size:16px;display:flex;align-items:center;justify-content:center;font-family:"Lato",sans-serif}

/* feature blocks */
.photo{position:absolute}
.frame{position:absolute;border:1.5px solid var(--red)}
.corner{position:absolute;border:1.5px solid #8a8a8a;background:#fff}
.h2{position:absolute;font-family:"Libre Caslon Text",serif;font-size:48px;color:var(--navy)}
.copy{position:absolute;font-size:15.5px;line-height:25.7px;color:#222}
.more{position:absolute;border:2px solid var(--navy);color:var(--navy);font-size:13px;font-weight:600;display:flex;align-items:center;justify-content:center}
.how-bg{left:0;top:1342px;width:1200px;height:591px;background:linear-gradient(180deg,#fff,#f3f3f6)}

/* philosophy band */
.phil{left:0;top:1933px;width:609px;height:385px;background:var(--grey);color:#fff}
.obj{left:609px;top:1933px;width:591px;height:385px;background:var(--navy);color:#fff}
.band-title{position:absolute;font-family:"Libre Caslon Text",serif;font-size:46px;color:#fff}
.band-copy{position:absolute;font-size:15.5px;line-height:25.7px;color:#fff}
.bullet{position:absolute;display:flex;gap:20px;font-size:15.5px;line-height:25.7px;color:#fff;width:440px}
.bullet i{flex:none;width:11px;height:11px;background:#fff;transform:rotate(45deg);margin-top:8px}

/* blogs */
.card{position:absolute;top:2502px;width:307px;height:390px;background:#fff;box-shadow:0 2px 10px rgba(0,0,0,.12);text-align:center}
.card .pic{height:208px}
.card .date{margin-top:22px;font-size:15px;color:#333}
.card .title{margin-top:12px;font-family:"Lato",sans-serif;font-size:20px;line-height:30px;color:var(--navy)}
.card .title strong{font-weight:700}
.card .read{position:absolute;bottom:24px;width:100%;font-size:13px;font-weight:600;color:var(--navy)}

/* contact */
.contact{left:0;top:3001px;width:1200px;height:597px;background:linear-gradient(180deg,#1c2060 0%,#2b3270 50%,#1a1e52 100%)}
.field{position:absolute;background:#fff;border-radius:8px;font-family:"Lato",sans-serif;font-size:18px;color:#666;padding:14px 27px}
.submit{position:absolute;left:495px;top:3478px;width:185px;height:59px;border:2px solid #fff;border-radius:8px;color:#fff;font-family:"Lato",sans-serif;font-size:22px;display:flex;align-items:center;justify-content:center}

/* newsletter + footer */
.news{left:0;top:3598px;width:1200px;height:104px;background:var(--navy-deep)}
.footer{left:0;top:3702px;width:1200px;height:270px;background:var(--navy)}
.copyright{position:absolute;top:3922px;width:1200px;text-align:center;font-family:"Lato",sans-serif;font-size:20px;color:#9b9cc0}
</style>
</head>
<body>

<!-- header -->
<div class="brand-box" style="left:450px;top:22px;width:300px;height:52px">FerolanVexa</div>
<div class="lang"><i></i>En</div>
<div class="abs" style="left:0;top:100px;width:1200px;height:70px;background:var(--navy)"></div>
<nav class="nav" style="top:100px;height:70px">
  <span>START</span><b>|</b><span>HOW WE WORK</span><b>|</b><span>SUCCESSFUL INVESTMENTS</span><b>|</b><span>CONTACT</span><b>|</b><span>PRESENT</span>
</nav>

<!-- hero -->
<section class="abs hero" role="img" aria-label="Madrid city street at dusk with historic domed building">
  <h1>Investment in Spain</h1>
  <div class="hero-sub">VEXA QUALITY INVESTMENT SL</div>
  <div class="hero-btn">GET STARTED</div>
</section>

<!-- about -->
<div class="frame" style="left:171px;top:953px;width:387px;height:369px"></div>
<div class="corner" style="left:509px;top:924px;width:63px;height:60px"></div>
<div class="photo" role="img" aria-label="Advisor smiling in a meeting with a client" style="left:154px;top:936px;width:387px;height:367px;background:linear-gradient(135deg,#dcdfe4,#9aa0a8 55%,#5d6068)"></div>
<h2 class="h2" style="left:609px;top:970px">About Us</h2>
<p class="copy" style="left:608px;top:1045px;width:430px">We are a great team of professionals and associated companies, in Spain and Latin America, with the mission of supporting you in your "Investment in Spain" project. We coordinate, supervise and manage the entire investment process so that non-resident foreigners can buy homes, commercial premises or make investments in companies and startups in Spain.</p>
<div class="more" style="left:608px;top:1249px;width:95px;height:30px">Read More</div>

<!-- how -->
<div class="abs how-bg"></div>
<h2 class="h2" style="left:140px;top:1491px">How do we do it?</h2>
<p class="copy" style="left:140px;top:1570px;width:432px">We study the best investment opportunities that are presented in Spain at all times: Real estate assets, commercial representations, startups and companies. We professionally support our clients throughout the investment process in Spain. We work effectively so that your investments in Spain are safe, profitable and allow you to obtain a residence visa in accordance with Law 14/2013.</p>
<div class="more" style="left:159px;top:1777px;width:94px;height:29px">Read More</div>
<div class="frame" style="left:643px;top:1456px;width:386px;height:367px"></div>
<div class="corner" style="left:632px;top:1428px;width:62px;height:59px"></div>
<div class="photo" role="img" aria-label="Hands reviewing financial charts on a tablet and papers" style="left:660px;top:1439px;width:386px;height:367px;background:linear-gradient(135deg,#1d3a66,#4c7fa8 50%,#b86b4a)"></div>

<!-- philosophy / objectives -->
<section class="abs phil">
  <h2 class="band-title" style="left:0;width:670px;text-align:center;top:52px">Our Philosophy</h2>
  <p class="band-copy" style="left:126px;top:140px;width:428px;text-align:center">We are a great team of professionals and associated companies, in Spain and Latin America, with the mission of supporting you in your "Investment in Spain" project. We coordinate, supervise and manage the entire investment process so that non-resident foreigners can buy homes, commercial premises or make investments in companies and startups in Spain.</p>
</section>
<section class="abs obj">
  <h2 class="band-title" style="left:96px;top:48px">Our&nbsp; Objectives</h2>
  <div class="bullet" style="left:84px;top:154px"><i></i><span>Find you the best and most profitable investment opportunities in Spain.</span></div>
  <div class="bullet" style="left:84px;top:224px"><i></i><span>Support you throughout the process with transparency, honesty and always seeking your highest profitability.</span></div>
</section>

<!-- blogs -->
<h2 class="h2" style="left:0;width:1210px;text-align:center;top:2400px">Recent Blogs</h2>
<article class="card" style="left:113px">
  <div class="pic" role="img" aria-label="Woman working on a laptop in a café" style="background:linear-gradient(135deg,#8a5a2c,#c8873e 50%,#6b2a22)"></div>
  <div class="date">Oct 8, 2022</div>
  <div class="title">Individuals access<br><strong>“FACTORING”</strong></div>
  <div class="read">Read More</div>
</article>
<article class="card" style="left:446px">
  <div class="pic" role="img" aria-label="Glass palace interior in a Madrid park" style="background:linear-gradient(180deg,#8c7a5e,#d9d3c8 50%,#b4574a)"></div>
  <div class="date">Oct 8, 2022</div>
  <div class="title">The projects that will<br>transform Madrid</div>
  <div class="read">Read More</div>
</article>
<article class="card" style="left:776px">
  <div class="pic" role="img" aria-label="Close-up portrait with digital overlay" style="background:linear-gradient(135deg,#9fb7c4,#d7e2e6 55%,#6f8796)"></div>
  <div class="date">Oct 8, 2022</div>
  <div class="title">DRIVALO Successful<br>financing</div>
  <div class="read">Read More</div>
</article>

<!-- contact -->
<section class="abs contact" role="img" aria-label="Madrid city street at night, darkened"></section>
<h2 class="abs serif" style="left:0;width:1210px;text-align:center;top:3050px;font-size:48px;color:#fff;font-weight:400">Contact Us</h2>
<div class="field" style="left:211px;top:3163px;width:384px;height:51px">First Name</div>
<div class="field" style="left:608px;top:3163px;width:384px;height:51px">Last Name</div>
<div class="field" style="left:211px;top:3231px;width:781px;height:50px">Email Id</div>
<div class="field" style="left:211px;top:3301px;width:781px;height:135px">Message</div>
<div class="submit">SUBMIT</div>

<!-- newsletter -->
<section class="abs news">
  <div class="abs" style="left:253px;top:36px;font-size:23px;font-weight:600;color:#fff">Subscribe For Newsletter</div>
  <div class="abs" style="left:574px;top:31px;width:328px;height:40px;background:#fff;border-radius:8px;font-size:13px;color:#555;padding:11px 14px">Your Email Address</div>
  <svg class="abs" style="left:920px;top:32px" width="38" height="38" viewBox="0 0 24 24" fill="none" stroke="#fff" stroke-width="1.6" stroke-linejoin="round"><path d="M22 2 2 10l8 3 3 8z"/><path d="M22 2 10 13"/></svg>
</section>

<!-- footer -->
<footer class="abs footer"></footer>
<div class="brand-box" style="left:460px;top:3745px;width:299px;height:52px;border-color:#fff">FerolanVexa</div>
<nav class="nav" style="top:3845px;height:36px">
  <span>START</span><b>|</b><span>HOW WE WORK</span><b>|</b><span>SUCCESSFUL INVESTMENTS</span><b>|</b><span>CONTACT</span><b>|</b><span>PRESENT</span>
</nav>
<div class="abs" style="left:111px;top:3901px;width:978px;height:1px;background:var(--line)"></div>
<div class="copyright">Copyrights 2022@ Ferolan Vexa | All rights received</div>

</body>
</html>
```